Commercial photographer, UAV drone photography & 360 walk-through visuals

I need a business card design that is minimalist but yet pretentiously creative. My target market are architects, designers, advertising agents and marketing managers. It is important to stress that though I am asking for a minimalist design it needs to have creative impact.

Target Market(s)

Architects, interiors designers, web-designers, artists

Contact Information for Business Card

Include my name, mobile [cell] number, email, web page and the company logo. Do not to include a postal address.

Colors

Designer to choose colors to be used in the design.

Requirements
Must have
• The following information is to be included:
• Miles Perrow
• Photographer
• m: 07812 593174
• e: miles@mpframeworks.co.uk
• w: mpframeworks.co.uk

```html
<!DOCTYPE html>
<html lang="en">
<head>
<meta charset="utf-8">
<title>MP Frameworks – Business Card</title>
<link href="https://fonts.googleapis.com/css2?family=Jost:wght@400;500;600&display=swap" rel="stylesheet">
<style>
  :root {
    --backdrop: #34383a;
    --card-dark: #000000;
    --card-light: #ffffff;
    --ink-light: #ffffff;
    --ink-dark: #1c1c1c;
    --accent-dark: #4d4d4d;
    --accent-light: #e6e6e6;
  }
  * { margin: 0; padding: 0; box-sizing: border-box; }
  html, body {
    width: 1200px;
    height: 1000px;
    overflow: hidden;
    background: var(--backdrop);
    font-family: "Jost", "Futura", sans-serif;
  }
  .card {
    position: absolute;
    width: 564px;
    height: 322px;
    overflow: hidden;
    box-shadow: 0 10px 24px rgba(0,0,0,0.45);
  }
  .card--front { left: 220px; top: 164px; background: var(--card-dark); }
  .card--back { left: 425px; top: 517px; background: var(--card-light); }

  .card__mark {
    position: absolute;
    border-radius: 50%;
  }
  .card--front .card__mark {
    left: 40px; top: 70px; width: 190px; height: 190px;
    background: var(--accent-dark);
  }
  .card--back .card__mark {
    left: 40px; top: 70px; width: 190px; height: 190px;
    background: var(--accent-light);
  }

  .wordmark {
    position: absolute;
    left: 258px;
    top: 146px;
    display: flex;
    align-items: center;
    gap: 10px;
    color: var(--ink-light);
    font-weight: 500;
    font-size: 27px;
    letter-spacing: 2px;
    line-height: 1;
    text-transform: uppercase;
  }
  .wordmark__dot {
    width: 14px; height: 14px;
    border-radius: 50%;
    background: var(--ink-light);
  }

  .holder {
    position: absolute;
    left: 304px;
    top: 52px;
    color: var(--ink-dark);
    font-weight: 600;
    font-size: 14px;
    letter-spacing: 4px;
    text-transform: uppercase;
  }
  .contact {
    position: absolute;
    left: 300px;
    top: 190px;
    list-style: none;
    color: var(--ink-dark);
    font-size: 17px;
  }
  .contact__item {
    display: flex;
    align-items: center;
    gap: 8px;
    height: 30px;
  }
  .contact__icon { width: 17px; height: 17px; flex: none; }
</style>
</head>
<body>
  <section class="card card--front" aria-label="Card front">
    <div class="card__mark" aria-hidden="true"></div>
    <div class="wordmark">
      <span class="wordmark__dot" aria-hidden="true"></span>
      <span class="wordmark__name">MP Frameworks</span>
    </div>
  </section>

  <section class="card card--back" aria-label="Card back">
    <div class="card__mark" aria-hidden="true"></div>
    <p class="holder">Miles Perrow</p>
    <ul class="contact">
      <li class="contact__item">
        <svg class="contact__icon" viewBox="0 0 24 24" aria-hidden="true"><path fill="#1c1c1c" d="M6.6 10.8a15.1 15.1 0 0 0 6.6 6.6l2.2-2.2a1 1 0 0 1 1-.25 11.4 11.4 0 0 0 3.6.57 1 1 0 0 1 1 1V20a1 1 0 0 1-1 1A17 17 0 0 1 3 4a1 1 0 0 1 1-1h3.5a1 1 0 0 1 1 1c0 1.25.2 2.45.57 3.57a1 1 0 0 1-.25 1z"/></svg>
        <span>07812 593174</span>
      </li>
      <li class="contact__item">
        <svg class="contact__icon" viewBox="0 0 24 24" aria-hidden="true"><path fill="#1c1c1c" d="M2 5h20v14H2z"/><path fill="none" stroke="#fff" stroke-width="1.6" d="M2.5 5.5 12 13l9.5-7.5"/></svg>
        <span>miles@mpframeworks.co.uk</span>
      </li>
      <li class="contact__item">
        <svg class="contact__icon" viewBox="0 0 24 24" aria-hidden="true"><g fill="none" stroke="#1c1c1c" stroke-width="1.8"><circle cx="12" cy="12" r="9.5"/><ellipse cx="12" cy="12" rx="4" ry="9.5"/><path d="M2.5 12h19M4 7h16M4 17h16"/></g></svg>
        <span>www.mpframeworks.co.uk</span>
      </li>
    </ul>
  </section>
</body>
</html>
```